Presentation Folder for dental clinic

We need a presentation folder design. The presentation folder is what we give to our patients with treatment plans, quotes, images, information sheets etc.
I have uploaded current stationary designs for assistance as well as a photo of our external sign design.
We are an upmarket dental clinic.
Professionalism and customer service is key to us.
We provide information in presentation folders to give to patients.
It needs to memorable and a statement to who we are.

Target Market(s)

Main patient base is Male and Female 40 years old to 70 years old

Industry/Entity Type

Dental Clinic

Font styles to use
Serif
Sans Serif

Requirements
Must have
• Design:
• -Professional
• -Timeless
• -Modern
• - Memorable
• - Statement (if a patient puts down the folder, it will be easily identifiable with as Morvel Dentals folder)
• Logo
• Address, phone, email, website
• Dr Leon Brisco name and degree details
• Colour scheme to match current logos and branding
• "Your Smile Our Passion" quote
Nice to have
• Services listed:
• - Sleep Dentistry
• - Happy Gas
• - Dental Implants
• - Cosmetic Dentistry
• - Oral Surgery
• - Clearotune
• - Teeth Whitening
• - General Dentistry
• - Childrens Dentistry
• See website www.morveldental.com.au
Should not have
• Dental cliche photos

```html
<!DOCTYPE html>
<html lang="en">
<head>
<meta charset="utf-8">
<title>Morvel Dentals – Presentation Folder</title>
<link rel="stylesheet" href="https://fonts.googleapis.com/css2?family=Lato:wght@300;400;700&display=swap">
<style>
  :root {
    --purple: #8a4a9c;
    --purple-deep: #7a3e8d;
    --panel-grey: #dcdcdc;
    --backdrop: #e6e6e6;
    --paper: #ffffff;
    --ink: #3f3f3f;
    --ink-soft: #6a6a6a;
    --photo-a: #c9c3bc;
    --photo-b: #4a4f5e;
  }
  * { box-sizing: border-box; margin: 0; padding: 0; }
  html, body { width: 1200px; height: 2647px; overflow: hidden; }
  body { background: var(--backdrop); font-family: "Lato", Arial, sans-serif; color: var(--ink); position: relative; }

  .folder { position: absolute; left: 50px; top: 868px; width: 1100px; height: 912px; }
  .folder-shapes { position: absolute; inset: 0; }

  .brand-name { position: absolute; left: 640px; top: 46px; width: 420px; text-align: right;
    font-size: 50px; font-weight: 700; color: var(--purple); letter-spacing: -0.5px; }

  .doctor-photo { position: absolute; left: 24px; top: 152px; width: 134px; height: 242px;
    background: linear-gradient(180deg, var(--photo-a) 0%, #b3aca5 45%, var(--photo-b) 100%); }

  .doctor-bio { position: absolute; left: 174px; top: 148px; width: 500px; color: #fff; }
  .doctor-bio h2 { font-size: 17px; font-weight: 700; margin-bottom: 6px; }
  .doctor-bio p { font-size: 12.5px; line-height: 1.4; font-weight: 400; margin-bottom: 10px; text-align: justify; }

  .tagline { position: absolute; left: 826px; top: 240px; color: #fff; font-size: 45px; line-height: 1.2; font-weight: 300; }
  .tagline b { font-weight: 700; }

  .contact-list { position: absolute; left: 38px; top: 576px; list-style: none; }
  .contact-list li { display: flex; align-items: flex-start; gap: 12px; font-size: 13px; line-height: 1.3; margin-bottom: 14px; color: var(--ink); }
  .contact-list svg { flex: none; width: 12px; height: 12px; margin-top: 2px; fill: var(--purple); }

  .opening-hours { position: absolute; left: 318px; top: 570px; padding-left: 14px; border-left: 2px solid var(--purple);
    list-style: none; height: 116px; }
  .opening-hours li { font-size: 13px; line-height: 23px; color: var(--ink); }

  .service-list { position: absolute; left: 830px; top: 568px; width: 260px; list-style: none;
    display: grid; grid-template-columns: 150px 110px; row-gap: 17px; }
  .service-list li { font-size: 13.5px; color: var(--ink); position: relative; padding-left: 14px; }
  .service-list li::before { content: ""; position: absolute; left: 0; top: 6px; width: 5px; height: 5px; border-radius: 50%; background: var(--purple); }
  .service-list li:nth-child(odd) { margin-left: var(--shift, 0); }
</style>
</head>
<body>
  <main class="folder">
    <svg class="folder-shapes" width="1100" height="912" viewBox="0 0 1100 912" aria-hidden="true">
      <!-- cover sheet -->
      <rect x="0" y="0" width="1100" height="730" fill="var(--paper)"/>
      <!-- biography band -->
      <polygon points="0,135 673,135 782,410 0,410" fill="var(--purple)"/>
      <!-- tagline panel -->
      <polygon points="703,135 1100,135 1100,410 808,410" fill="var(--purple)"/>
      <!-- services panel -->
      <polygon points="818,505 1100,505 1100,730 703,730" fill="var(--panel-grey)"/>
      <!-- pocket flap -->
      <path d="M0,730 H520 C520,770 500,790 470,790 H160 C130,790 120,805 120,830 V912 H30 C12,912 0,900 0,882 Z" fill="var(--paper)"/>
      <line x1="120" y1="800" x2="170" y2="800" stroke="#cfcfcf" stroke-dasharray="4 4"/>
      <line x1="120" y1="870" x2="170" y2="870" stroke="#cfcfcf" stroke-dasharray="4 4"/>
    </svg>

    <div class="brand-name">Morvel Dentals</div>

    <div class="doctor-photo" role="img" aria-label="Portrait photograph of Dr Leon Brisco"></div>

    <section class="doctor-bio">
      <h2>Dr Leon Brisco</h2>
      <p>Dr Leon Brisco was born and raised in England. He graduated from Westbridge College, University of Lenford in 1995. He gained further qualifications in the USA and then worked in general practice in England.<br>
      Dr Leon has advanced training in Intravenous Sedation, Happy Gas, Cosmetic Dentistry, Implants, Bone grafting, Sinus lifts, Oral Surgery and Clearotune. All of these multi-skills enable him to be able to look after and be solely responsible for his patients.</p>
      <p>Outside of dentistry he is a self-confessed sports nut! He plays squash and golf. He is quite a philosophical character and shares this gem with us.<br>
      "Love the job you do, and you never have to work again!" He feels that he has achieved this with his dentistry, and is enjoying providing excellent care.</p>
      <p>Dr Leon will always, "Do unto others as you would have others do unto you".</p>
    </section>

    <h1 class="tagline"><b>Your</b> Smile<br>Our <b>Passion</b></h1>

    <ul class="contact-list">
      <li><svg viewBox="0 0 12 12"><path d="M6 0a4 4 0 0 0-4 4c0 3 4 8 4 8s4-5 4-8a4 4 0 0 0-4-4zm0 5.5A1.5 1.5 0 1 1 6 2.5a1.5 1.5 0 0 1 0 3z"/></svg>
        <span>214 Harbour Rd, Brightvale, VIC, 3190<br>(Car Park and Reception Entry via Kelby Road)</span></li>
      <li><svg viewBox="0 0 12 12"><path d="M2.5 0.5l2 2-1 1.5c.7 1.6 2 2.9 3.5 3.5l1.5-1 2 2-1.2 2C4.5 10.4 1.6 7.5 .5 1.7z"/></svg><span>03 9000 4417</span></li>
      <li><svg viewBox="0 0 12 12"><path d="M0 2h12v8H0zM1 3l5 3.5L11 3v-.2H1z" fill-rule="evenodd"/></svg><span>info@morveldental.com.au</span></li>
      <li><svg viewBox="0 0 12 12"><circle cx="6" cy="6" r="5.5"/><path d="M.5 6h11M6 .5c-2 2-2 9 0 11M6 .5c2 2 2 9 0 11" stroke="#fff" stroke-width=".8" fill="none"/></svg><span>www.morveldental.com.au</span></li>
    </ul>

    <ul class="opening-hours">
      <li>Monday 9:00am – 5:00pm</li>
      <li>Tuesday 9:00am – 7:00pm</li>
      <li>Wednesday 9:00am – 1:00pm</li>
      <li>Thursday 8:00am – 5:00pm</li>
      <li>Friday 7:30am – 2:00pm</li>
    </ul>

    <ul class="service-list">
      <li style="--shift:26px">Sleep Dentistry</li>
      <li>Happy Gas</li>
      <li style="--shift:18px">Cosmetic Dentistry</li>
      <li>Dental Implants</li>
      <li style="--shift:8px">General Dentistry</li>
      <li>Children's Dentistry</li>
      <li>Clearotune</li>
      <li style="margin-left:-30px">Teeth Whitening</li>
    </ul>
  </main>
</body>
</html>
```